Need simple and modern looking business card with all my information on one side and logo on the other side
Info :
Company name - VELMAR CONSTRUCTION LLC
Company addres- 418 harbor 87th. Dunmoor park ny 10352
Email- velmarllc@tridomail.Com
Company phone number 555-318-6094
Cell number- 555-742-0583
Web site - velmarllc.Com
My name Gerald tomasino

Target Market(s)

Construction , home improvement, remodeling

Industry/Entity Type

Construction

Contact Information for Business Card

It has to be moder but at the same time simple

Font styles to use
Sans Serif

Colors
0255a3
ffffff
000000
f78f20
b1b1b1
9d9d9d
1b1b1b
33a6d7
ec1f27

Requirements
Must have
• My logo on one side maybe with a some kind of background on the other side all my information
Nice to have
• Some kind of background pictures provided by you .PLEASE HAVE ACCOUNT WITH PIXELVAULT WILL NOT PAY ANY EXTRA FEES .
Should not have
• Any kind of hamer, nails,screws, helmets itp. Please do not copy the other designs come up with something new.

```html
<!DOCTYPE html>
<html lang="en">
<head>
<meta charset="utf-8">
<title>Gerald Tomasino – Business Card</title>
<link rel="stylesheet" href="https://fonts.googleapis.com/css2?family=Didact+Gothic&display=swap">
<style>
  :root {
    --ink: #1b1b1b;
    --title-blue: #1f3f8a;
    --panel-light: #213f86;
    --panel-dark: #0b1532;
    --band-grey: #c9c6c6;
    --corner-grey: #b1b1b1;
    --corner-soft: #e9e9e9;
    --hazard-orange: #f7a11e;
    --hazard-black: #1b1b1b;
    --sky-top: #4f86e6;
    --sky-bottom: #9cc0f2;
    --tower: #c9c1ae;
    --white: #ffffff;
  }
  * { margin: 0; padding: 0; box-sizing: border-box; }
  html, body { width: 1200px; height: 741px; overflow: hidden; background: var(--white); }
  .card {
    position: relative;
    width: 1200px;
    height: 741px;
    background: var(--white);
    font-family: "Didact Gothic", "Century Gothic", sans-serif;
    overflow: hidden;
  }
  .card__art { position: absolute; inset: 0; width: 1200px; height: 741px; }
  .card__identity {
    position: absolute;
    left: 560px;
    width: 540px;
    top: 104px;
    text-align: center;
  }
  .card__name {
    font-size: 31px;
    font-weight: 400;
    color: var(--ink);
    letter-spacing: 0.5px;
    line-height: 1.15;
  }
  .card__role {
    font-size: 25px;
    color: var(--title-blue);
    line-height: 1.2;
  }
  .card__contacts {
    position: absolute;
    left: 507px;
    top: 236px;
    list-style: none;
    color: var(--white);
    font-size: 30px;
    line-height: 56.5px;
    letter-spacing: 0.3px;
  }
</style>
</head>
<body>
<div class="card">
  <svg class="card__art" viewBox="0 0 1200 741" aria-hidden="false">
    <defs>
      <linearGradient id="sky" x1="0" y1="0" x2="0" y2="1">
        <stop offset="0" stop-color="var(--sky-top)"/>
        <stop offset="1" stop-color="var(--sky-bottom)"/>
      </linearGradient>
      <linearGradient id="tower" x1="0" y1="0" x2="1" y2="0">
        <stop offset="0" stop-color="#a9a392"/>
        <stop offset="0.5" stop-color="var(--tower)"/>
        <stop offset="1" stop-color="#8f8a7d"/>
      </linearGradient>
      <radialGradient id="panel" cx="0.25" cy="0.3" r="0.9">
        <stop offset="0" stop-color="var(--panel-light)"/>
        <stop offset="1" stop-color="var(--panel-dark)"/>
      </radialGradient>
      <pattern id="hazard" width="20" height="40" patternUnits="userSpaceOnUse" patternTransform="skewY(-35)">
        <rect width="20" height="20" fill="var(--hazard-orange)"/>
        <rect y="20" width="20" height="20" fill="var(--hazard-black)"/>
      </pattern>
    </defs>

    <g class="tower-photo" role="img" aria-label="Photo of a tall residential glass tower against a blue sky">
      <rect x="0" y="0" width="455" height="741" fill="url(#sky)"/>
      <rect x="10" y="40" width="425" height="701" fill="url(#tower)" opacity="0.9"/>
    </g>

    <rect class="hazard-strip" x="453" y="0" width="20" height="741" fill="url(#hazard)"/>

    <polygon class="corner corner--top" points="1135,0 1200,0 1200,95" fill="var(--corner-grey)"/>
    <polygon class="corner corner--bottom" points="1200,598 1200,741 1140,741" fill="var(--corner-soft)"/>

    <rect class="panel-band" x="473" y="193" width="727" height="363" fill="var(--band-grey)"/>
    <polygon class="panel-band-tip" points="473,193 473,556 402,372" fill="var(--band-grey)"/>
    <polygon class="contact-panel" points="484,203 1200,203 1200,548 484,548 412,372" fill="url(#panel)"/>
  </svg>

  <header class="card__identity">
    <h1 class="card__name">GERALD TOMASINO</h1>
    <p class="card__role">Construction Manager</p>
  </header>

  <ul class="card__contacts">
    <li>418 harbor 87th, Dunmoor park ny 10352</li>
    <li>E-mail - velmarllc@tridomail.com</li>
    <li>Company number- 555-318-6094</li>
    <li>Cell number- 555-742-0583</li>
    <li>Website: velmarllc.com</li>
  </ul>
</div>
</body>
</html>
```